Structural Engineering Company needs ad for magazine

We are an engineering office for structural engineering in the entertainment industry. Our focus are concert stages, festival structures, grand stands and exhibition booths. Our customers are mainly from Europe, we realize the projects worldwide. Typical customers are designer, architects, stage builders, exhibition builder and technical service provider. We are creating structural analyses, technical consulting, technical drawings and risk assessment. We are working on mid size and major events.
Some technical notes:
- CMYK profile needed, minimum 300 dpi for raster graphic
- Our primary color is Petrol. Favourite is petrol, coral and grey (black). Please use palette shown below.
- Our font in documents is Myriad. Regular at 10 pt for text and Light at 16-24pt for titles.
- The format for the ad is 61 x 127 mm (portrait) or 185 x 46 mm (landscape). Which one is up to you.
To the content:
- For contact details we just want to provide our web address "falkowerk.de" and/or our e-mail "info@falkowerk.de"
- Attached are some Logo files and photos.
- The ad do not advertise a specific product. It is more a general advertisement for the company.
- The language for the ad should be German. Below are keywords in English and corresponding German translation. You do not need to place all Keywords, it is just a brainstorming list to help you. You are also welcome to use other text. We will help with translation, if necessary.
- we like discussing ideas to get better results, so also if you have questions, please ask.
- If you need information that we haven't thought of yet, please ask.
Our slogan (also in Germany): event meets engineering
Service Keywords EN / DE
- Structural Analysis / Statische Berechnungen
- Risk Assessment / Risikobewertungen
- Consulting & Design / Beratung & Konstruktion
Technical Keywords EN / DE
- Stage machinery / Bühnentechnik
- Scaffolding / Gerüstbau
- Exhibition Booths / Messebauten
- Tents / Zelte
- Temporary Structures / Fliegende Bauten
- Truss / Traversen
- Stages / Bühnen
- Grand Stands / Tribünen
- Leightweight Construction / Leichtbau
- Steel Construction / Stahlbau
- Amusement Rides / Fahrgeschäfte
Look and feel

```html
<!DOCTYPE html>
<html lang="de">
<head>
<meta charset="utf-8">
<title>Falkowerk – Event meets Engineering</title>
<link href="https://fonts.googleapis.com/css2?family=Montserrat:wght@400;500;600;700&display=swap" rel="stylesheet">
<style>
  :root{
    --teal:#5ee9da;
    --pink:#f7548f;
    --ink:#2b2b2b;
    --white:#ffffff;
    --page:#ffffff;
    --photo-grey:#6d7f86;
  }
  *{margin:0;padding:0;box-sizing:border-box}
  html,body{width:1200px;height:400px;overflow:hidden;background:var(--page)}
  body{font-family:'Montserrat',sans-serif;color:var(--ink);position:relative}
  .ad{position:absolute;left:121px;top:71px;width:974px;height:242px;background:var(--white);
      box-shadow:0 2px 5px rgba(0,0,0,.35);overflow:hidden}
  .shapes{position:absolute;left:0;top:0}
  .slogan{position:absolute;left:13px;top:6px;font-size:40px;font-weight:700;line-height:40px;color:var(--teal);white-space:nowrap}
  .slogan-box{position:absolute;left:316px;top:6px;width:281px;height:40px;background:var(--pink);
      color:var(--white);font-size:37px;font-weight:500;line-height:41px;text-align:center;white-space:nowrap}
  .heading{position:absolute;top:65px;font-size:15px;font-weight:700;line-height:16px;white-space:nowrap}
  .heading--services{left:14px;color:var(--teal)}
  .heading--technical{left:147px;color:var(--pink)}
  .item{position:absolute;font-size:9.3px;line-height:11px;white-space:nowrap;color:var(--ink)}
  .item--service{font-size:9.5px;line-height:11.3px}
  .tick{position:absolute;width:8.5px;height:8.5px}
  .photo{position:absolute;top:157px;width:109px;height:76px;border:3px solid var(--teal);border-radius:3px;padding:2px;background:var(--white)}
  .photo span{display:block;width:100%;height:100%}
  .photo--light span{background:linear-gradient(135deg,#3b2a9a,#7b5cff 50%,#cfc6ff)}
  .photo--crowd span{background:linear-gradient(180deg,#4a5a4a,#b8324a 55%,#3a2a2a)}
  .photo--build span{background:linear-gradient(180deg,#4d6d8c,#5f7890 50%,#d9d9d9)}
  .photo--dome span{background:linear-gradient(180deg,#6a8a4a,#d8c29a 55%,#8a8a7a)}
  .brand{position:absolute;left:0;top:218px;width:103px;text-align:center;color:var(--white);font-size:8.5px;font-weight:600;letter-spacing:1.5px}
  .contact{position:absolute;color:var(--ink);white-space:nowrap}
  .contact--phone{left:761px;top:192px;font-size:10px;font-weight:500}
  .contact--mail{left:763px;top:210px;font-size:7.8px}
  .contact--web{left:763px;top:225px;font-size:7.8px}
  .contact--address{left:903px;top:193px;font-size:7.4px;line-height:9px}
  .icon{position:absolute;width:10px;height:10px}
</style>
</head>
<body>
<div class="ad">
  <svg class="shapes" width="974" height="242" viewBox="0 0 974 242">
    <polygon points="0,191 127,191 103,242 0,242" fill="var(--teal)"/>
    <polygon points="660,0 667,0 613,184 605,184" fill="var(--teal)"/>
    <polygon points="667,0 974,0 974,184 613,184" fill="var(--photo-grey)" role="img" aria-label="Foto: Stahl- und Traversenkonstruktion einer Bühne im Stadion"/>
    <polygon points="723,184 974,184 974,242 700,242" fill="var(--pink)"/>
  </svg>

  <div class="slogan">EVENT MEETS</div>
  <div class="slogan-box">ENGINEERING</div>

  <div class="heading heading--services">OUR SERVICES</div>
  <div class="heading heading--technical">TECHNICAL SERVICES</div>

  <!-- services -->
  <svg class="tick" style="left:14px;top:92px" viewBox="0 0 10 10"><circle cx="5" cy="5" r="5" fill="var(--pink)"/><path d="M2.7 5.2l1.6 1.6 3-3.2" stroke="#fff" stroke-width="1.3" fill="none"/></svg>
  <div class="item item--service" style="left:29px;top:89px">Statische<br>Berechnungen</div>
  <svg class="tick" style="left:14px;top:125px" viewBox="0 0 10 10"><circle cx="5" cy="5" r="5" fill="var(--pink)"/><path d="M2.7 5.2l1.6 1.6 3-3.2" stroke="#fff" stroke-width="1.3" fill="none"/></svg>
  <div class="item item--service" style="left:30px;top:121px">Beratung &amp;<br>Konstruktion</div>
  <svg class="tick" style="left:14px;top:156px" viewBox="0 0 10 10"><circle cx="5" cy="5" r="5" fill="var(--pink)"/><path d="M2.7 5.2l1.6 1.6 3-3.2" stroke="#fff" stroke-width="1.3" fill="none"/></svg>
  <div class="item item--service" style="left:29px;top:152px">Risik<br>obewertungen</div>

  <!-- technical row 1 -->
  <svg class="tick" style="left:148px;top:89px" viewBox="0 0 10 10"><circle cx="5" cy="5" r="5" fill="var(--pink)"/><path d="M2.7 5.2l1.6 1.6 3-3.2" stroke="#fff" stroke-width="1.3" fill="none"/></svg>
  <div class="item" style="left:163px;top:88px">Bühnentechnik</div>
  <svg class="tick" style="left:241px;top:89px" viewBox="0 0 10 10"><circle cx="5" cy="5" r="5" fill="var(--pink)"/><path d="M2.7 5.2l1.6 1.6 3-3.2" stroke="#fff" stroke-width="1.3" fill="none"/></svg>
  <div class="item" style="left:258px;top:88px">Leichtbau</div>
  <svg class="tick" style="left:313px;top:90px" viewBox="0 0 10 10"><circle cx="5" cy="5" r="5" fill="var(--pink)"/><path d="M2.7 5.2l1.6 1.6 3-3.2" stroke="#fff" stroke-width="1.3" fill="none"/></svg>
  <div class="item" style="left:327px;top:89px">Gerüstbau</div>
  <svg class="tick" style="left:387px;top:91px" viewBox="0 0 10 10"><circle cx="5" cy="5" r="5" fill="var(--pink)"/><path d="M2.7 5.2l1.6 1.6 3-3.2" stroke="#fff" stroke-width="1.3" fill="none"/></svg>
  <div class="item" style="left:406px;top:90px">Fliegende Bauten</div>
  <svg class="tick" style="left:494px;top:92px" viewBox="0 0 10 10"><circle cx="5" cy="5" r="5" fill="var(--pink)"/><path d="M2.7 5.2l1.6 1.6 3-3.2" stroke="#fff" stroke-width="1.3" fill="none"/></svg>
  <div class="item" style="left:508px;top:91px">Tribünen</div>
  <svg class="tick" style="left:558px;top:92px" viewBox="0 0 10 10"><circle cx="5" cy="5" r="5" fill="var(--pink)"/><path d="M2.7 5.2l1.6 1.6 3-3.2" stroke="#fff" stroke-width="1.3" fill="none"/></svg>
  <div class="item" style="left:571px;top:91px">Zelte</div>

  <!-- technical row 2 -->
  <svg class="tick" style="left:148px;top:109px" viewBox="0 0 10 10"><circle cx="5" cy="5" r="5" fill="var(--pink)"/><path d="M2.7 5.2l1.6 1.6 3-3.2" stroke="#fff" stroke-width="1.3" fill="none"/></svg>
  <div class="item" style="left:163px;top:108px">Fahrgeschäfte</div>
  <svg class="tick" style="left:240px;top:109px" viewBox="0 0 10 10"><circle cx="5" cy="5" r="5" fill="var(--pink)"/><path d="M2.7 5.2l1.6 1.6 3-3.2" stroke="#fff" stroke-width="1.3" fill="none"/></svg>
  <div class="item" style="left:258px;top:108px">Stahlbau</div>
  <svg class="tick" style="left:313px;top:110px" viewBox="0 0 10 10"><circle cx="5" cy="5" r="5" fill="var(--pink)"/><path d="M2.7 5.2l1.6 1.6 3-3.2" stroke="#fff" stroke-width="1.3" fill="none"/></svg>
  <div class="item" style="left:328px;top:109px">Traversen</div>
  <svg class="tick" style="left:387px;top:109px" viewBox="0 0 10 10"><circle cx="5" cy="5" r="5" fill="var(--pink)"/><path d="M2.7 5.2l1.6 1.6 3-3.2" stroke="#fff" stroke-width="1.3" fill="none"/></svg>
  <div class="item" style="left:406px;top:108px">Messebauten</div>
  <svg class="tick" style="left:494px;top:110px" viewBox="0 0 10 10"><circle cx="5" cy="5" r="5" fill="var(--pink)"/><path d="M2.7 5.2l1.6 1.6 3-3.2" stroke="#fff" stroke-width="1.3" fill="none"/></svg>
  <div class="item" style="left:509px;top:109px">Bühnen</div>

  <!-- project photos -->
  <div class="photo photo--light" style="left:146px"><span role="img" aria-label="Foto: Traverse mit Bühnenscheinwerfern"></span></div>
  <div class="photo photo--crowd" style="left:259px"><span role="img" aria-label="Foto: Festivalbühne mit Publikum"></span></div>
  <div class="photo photo--build" style="left:372px"><span role="img" aria-label="Foto: Bühnenaufbau im Stadion"></span></div>
  <div class="photo photo--dome" style="left:485px"><span role="img" aria-label="Foto: Holzpavillons im Park"></span></div>

  <div class="brand">FALKOWERK</div>

  <!-- contact -->
  <svg class="icon" style="left:748px;top:193px" viewBox="0 0 10 10"><circle cx="5" cy="5" r="5" fill="#fff"/><path d="M3 2.4l1.1 1.4-.6.7c.4.9 1.1 1.6 2 2l.7-.6 1.4 1.1-.6 1c-2.5-.3-4.4-2.2-4.7-4.7z" fill="var(--ink)"/></svg>
  <div class="contact contact--phone">49 (0) 30 / 55 20 41 70</div>
  <svg class="icon" style="left:748px;top:210px" viewBox="0 0 10 10"><circle cx="5" cy="5" r="5" fill="#fff"/><rect x="2.6" y="3.3" width="4.8" height="3.4" fill="none" stroke="var(--ink)" stroke-width=".8"/><path d="M2.6 3.3l2.4 2 2.4-2" fill="none" stroke="var(--ink)" stroke-width=".8"/></svg>
  <div class="contact contact--mail">info@falkowerk.de</div>
  <svg class="icon" style="left:748px;top:225px" viewBox="0 0 10 10"><circle cx="5" cy="5" r="5" fill="#fff"/><circle cx="5" cy="5" r="2.6" fill="none" stroke="var(--ink)" stroke-width=".7"/><path d="M2.4 5h5.2M5 2.4c-1.2 1.5-1.2 3.7 0 5.2M5 2.4c1.2 1.5 1.2 3.7 0 5.2" fill="none" stroke="var(--ink)" stroke-width=".6"/></svg>
  <div class="contact contact--web">www.falkowerk.de</div>
  <svg class="icon" style="left:890px;top:193px" viewBox="0 0 10 10"><circle cx="5" cy="5" r="5" fill="#fff"/><path d="M5 8.2C3.4 6.3 2.8 5.3 2.8 4.2a2.2 2.2 0 0 1 4.4 0c0 1.1-.6 2.1-2.2 4z" fill="var(--ink)"/><circle cx="5" cy="4.2" r=".8" fill="#fff"/></svg>
  <div class="contact contact--address">Lindenweg 12<br>10115 Berlin<br>GERMANY</div>
</div>
</body>
</html>
```